Re-design of an existing website

We are needing a redesign of http://www.corvane-pharmacy.com/. Same colour scheme and content. The design needs to be done using Zurb Foundation 5 with all SCSS included and setup accordingly.

Placeholder images may be used for now as photo's are in progress. Must be responsive and work on all device types.
Updates

PLEASE NOTE: The project manager is currently on holidays until the 6th of September, hopefully we will have a decision closer to this date but it may be a few days after.

Industry/Entity Type

Medical

Coding

Coded - Design and coding required

Number of Pages Required

3 page

Font styles to use
Sans Serif

Requirements
Must have
• Zurb Foundation 5

```html
<!DOCTYPE html>
<html lang="en">
<head>
<meta charset="utf-8">
<title>The Corvane Pharmacy</title>
<link rel="stylesheet" href="https://fonts.googleapis.com/css2?family=Open+Sans:ital,wght@0,400;0,600;0,700;1,400&display=swap">
<style>
:root{
  --navy:#1b2f6b;
  --navy-dark:#10204d;
  --blue:#2b4a9a;
  --ink:#333a44;
  --muted:#6b7280;
  --line:#d9dde5;
  --hero:#eef0f4;
  --map:#e3e6ea;
  --white:#ffffff;
}
*{box-sizing:border-box;margin:0;padding:0}
html,body{width:841px;height:1200px;overflow:hidden}
body{font-family:"Open Sans",Arial,sans-serif;color:var(--ink);background:var(--white);font-size:9px;line-height:1.5}
.page{position:relative;width:841px;height:1200px}

.site-header{height:60px;display:flex;align-items:flex-end;justify-content:space-between;padding:0 32px 10px}
.brand{display:flex;align-items:center;gap:8px}
.brand-mark{width:26px;height:26px;border-radius:50%;background:var(--navy)}
.brand-name{font-size:16px;font-weight:700;color:var(--navy);line-height:1.1}
.brand-tag{font-size:7px;color:var(--navy);font-style:italic}
.header-right{display:flex;flex-direction:column;align-items:flex-end;gap:8px}
.search{width:120px;height:16px;border:1px solid var(--line);display:flex;justify-content:flex-end;align-items:center;padding-right:4px}
.main-nav{display:flex;gap:18px;font-size:8px;color:var(--navy);font-weight:600}

.hero{position:relative;height:330px;background:var(--hero);overflow:hidden}
.hero-photo{position:absolute;left:380px;top:0;width:420px;height:330px;background:linear-gradient(120deg,#f3f1ee,#e9d8c8 45%,#f4f5f7)}
.hero-copy{position:absolute;left:70px;top:160px;width:300px}
.hero-copy h1{font-size:34px;font-weight:400;color:#3d4a63;line-height:1.1;margin-bottom:10px}
.hero-copy p{font-size:8px;color:var(--muted)}
.hero-arrow{position:absolute;top:150px}
.hero-arrow.left{left:12px}.hero-arrow.right{right:12px}

.service-nav{position:absolute;top:392px;left:0;width:841px;height:28px;background:var(--navy);display:flex;justify-content:center;gap:0}
.service-nav span{color:var(--white);font-size:8px;font-weight:600;padding:0 15px;line-height:28px;border-right:1px solid rgba(255,255,255,.2)}
.service-nav span:last-child{border-right:0}

.welcome{position:absolute;top:438px;left:100px;width:641px;text-align:center}
.welcome h2{font-size:20px;font-weight:400;color:#3d4a63;margin-bottom:8px}
.welcome p{font-size:7.5px;color:var(--muted)}

.cards{position:absolute;top:540px;left:70px;width:701px;display:flex;gap:17px}
.card{width:162px}
.card-img{height:110px;margin-bottom:8px}
.card h3{font-size:10px;font-weight:600;color:var(--ink);margin-bottom:4px}
.card p{font-size:7.5px;color:var(--muted);margin-bottom:8px}
.btn{display:inline-block;background:var(--navy);color:var(--white);font-size:7.5px;padding:4px 12px}

.info{position:absolute;top:760px;left:0;width:841px;height:375px;background:var(--map)}
.info-map{position:absolute;inset:0;background:linear-gradient(135deg,#e8eaee,#dfe3e8 50%,#e9ebef)}
.info-cols{position:absolute;top:30px;left:70px;width:701px;display:flex;gap:28px}
.info-col{width:215px}
.info-col h2{font-size:17px;font-weight:400;color:#3d4a63;margin-bottom:10px}
.info-col p{font-size:7.5px;color:var(--muted);margin-bottom:12px}
.news li{list-style:none;font-size:7.5px;color:var(--ink);margin-bottom:12px}
.news small{display:block;color:var(--muted);font-size:7px}
.hours{background:var(--white);padding:10px 12px;font-size:7.5px}
.hours b{display:block;color:var(--ink);margin-top:6px}
.hours span{color:var(--muted)}
.map-btn{position:absolute;right:30px;bottom:8px;background:var(--navy);color:var(--white);font-size:7px;padding:4px 10px}

.site-footer{position:absolute;top:1135px;left:0;width:841px;height:65px;background:var(--navy-dark);color:var(--white)}
.contact{position:absolute;left:360px;top:12px;font-size:7.5px;line-height:1.8}
.contact div{display:flex;align-items:center;gap:5px}
.social{position:absolute;right:40px;top:18px;display:flex;gap:5px}
.social i{width:12px;height:12px;border-radius:50%;background:#3c5599;display:block}
.copy{position:absolute;left:24px;bottom:6px;font-size:6.5px;color:#aeb7d0}
</style>
</head>
<body>
<div class="page">
  <header class="site-header">
    <div class="brand">
      <span class="brand-mark"></span>
      <div>
        <div class="brand-name">The Corvane Pharmacy</div>
        <div class="brand-tag">"Trusted Care For Every Need"</div>
      </div>
    </div>
    <div class="header-right">
      <div class="search">
        <svg width="8" height="8" viewBox="0 0 10 10"><circle cx="4" cy="4" r="3" fill="none" stroke="#1b2f6b" stroke-width="1.3"/><line x1="6.3" y1="6.3" x2="9" y2="9" stroke="#1b2f6b" stroke-width="1.3"/></svg>
      </div>
      <nav class="main-nav"><span>Home</span><span>Brochures</span><span>Employment</span><span>Opening Hours &amp; Directions</span><span>Contact Us</span></nav>
    </div>
  </header>

  <section class="hero">
    <div class="hero-photo" role="img" aria-label="Photo of a mother holding her baby"></div>
    <div class="hero-copy">
      <h1>Mother And Baby</h1>
      <p>Friendly advice and trusted products for new mothers and their babies, from feeding support to everyday health care, all available from our caring pharmacy team.</p>
    </div>
    <svg class="hero-arrow left" width="14" height="30" viewBox="0 0 14 30"><polyline points="12,2 2,15 12,28" fill="none" stroke="#9aa3b2" stroke-width="2"/></svg>
    <svg class="hero-arrow right" width="14" height="30" viewBox="0 0 14 30"><polyline points="2,2 12,15 2,28" fill="none" stroke="#9aa3b2" stroke-width="2"/></svg>
  </section>

  <nav class="service-nav">
    <span>Community Pharmacy</span><span>CPAP</span><span>Milk</span><span>Oncology Service</span><span>Home Nursing</span><span>Nutrition</span><span>Compounding</span><span>Surgical Supply</span>
  </nav>

  <section class="welcome">
    <h2>Welcome to our website</h2>
    <p>Our pharmacy has served the local community for many years, offering professional advice, prescription services and a wide range of health products. Our experienced staff take time to listen and help you find the right care for you and your family. Visit us in store or browse our services below to learn more about everything we offer, from specialist compounding to home nursing support and sleep care solutions.</p>
  </section>

  <section class="cards">
    <article class="card">
      <div class="card-img" role="img" aria-label="Photo of oncology medication preparation" style="background:linear-gradient(135deg,#c9d3e3,#e8c9c2)"></div>
      <h3>Oncology Services</h3>
      <p>Specialist preparation and support for patients undergoing cancer treatment.</p>
      <span class="btn">Read more</span>
    </article>
    <article class="card">
      <div class="card-img" role="img" aria-label="Photo of a sleep apnoea mask" style="background:linear-gradient(135deg,#dfe4ec,#b9c4d6)"></div>
      <h3>Sleep Apnoea</h3>
      <p>CPAP equipment, fittings and advice to help you enjoy a better night's rest.</p>
      <span class="btn">Read more</span>
    </article>
    <article class="card">
      <div class="card-img" role="img" aria-label="Photo of pharmacists compounding medicine" style="background:linear-gradient(135deg,#cfe0ea,#a9c4d8)"></div>
      <h3>Pharmaceutical Compounding</h3>
      <p>Custom medicines prepared on site to suit individual patient needs.</p>
      <span class="btn">Read more</span>
    </article>
    <article class="card">
      <div class="card-img" role="img" aria-label="Photo of a home nursing visit" style="background:linear-gradient(135deg,#d7e2ee,#9fb7d2)"></div>
      <h3>Home Nursing</h3>
      <p>Supplies and support so patients can be cared for comfortably at home.</p>
      <span class="btn">Read more</span>
    </article>
  </section>

  <section class="info">
    <div class="info-map" role="img" aria-label="Street map showing the pharmacy location"></div>
    <div class="info-cols">
      <div class="info-col">
        <h2>Celebrating 38 Years</h2>
        <p>Since first opening our doors, The Corvane Pharmacy has been offering friendly service, professional advice and the medicines our local community relies on. We are proud to have served three generations of families.</p>
        <span class="btn">Read more</span>
      </div>
      <div class="info-col">
        <h2>Health News</h2>
        <ul class="news">
          <li>Simple habits for a healthy heart this winter<small>Health Update</small></li>
          <li>Understanding your medication labels<small>Pharmacy Notes</small></li>
          <li>Tips for staying active as you get older<small>Wellbeing Weekly</small></li>
        </ul>
      </div>
      <div class="info-col">
        <h2>Opening Hours</h2>
        <div class="hours">
          <strong>We are open every day of the year.</strong>
          <b>Monday to Friday</b><span>7:00am to 9:00pm</span>
          <b>Saturday</b><span>8:00am to 7:00pm</span>
          <b>Sunday and Public Holidays</b><span>9:00am to 6:00pm</span>
        </div>
      </div>
    </div>
    <span class="map-btn">View larger map</span>
  </section>

  <footer class="site-footer">
    <div class="contact">
      <div><svg width="8" height="8" viewBox="0 0 10 10"><path d="M2 1l2 0 1 2.5-1.2 1a6 6 0 0 0 2.7 2.7l1-1.2L10 7v2c0 .6-.5 1-1 1A9 9 0 0 1 0 2c0-.5.4-1 1-1z" fill="#fff"/></svg>+61 (02) 5550 1938</div>
      <div><svg width="9" height="7" viewBox="0 0 10 8"><rect x=".5" y=".5" width="9" height="7" fill="none" stroke="#fff"/><polyline points=".5,.5 5,4.5 9.5,.5" fill="none" stroke="#fff"/></svg>hello@corvanepharmacy.example</div>
    </div>
    <div class="social"><i></i><i></i><i></i></div>
    <div class="copy">Copyright © 2014 all rights reserved</div>
  </footer>
</div>
</body>
</html>
```